Professional, modern and unique business card. We are looking to present a new look to our business cards however we don't want to divert too far away from original template. We want social media links and our 3 office addresses on the backside of the business cards. Please see attached business card templates for ideas.
Cobalt Homes Color Code:
R: 7
G:63
B:86

Target Market(s)

Real Estate

Industry/Entity Type

Real Estate

Contact Information for Business Card

Follow the attached templates. In need of a more modern and unique touch but don't want to divert from the original theme or color.
Cobalt Homes Color Code:
R: 7
G:63
B:86

Font styles to use
Serif

Requirements
Must have
• Cobalt Homes logo, Cobalt homes colors, social media links, 3 office addresses,
Nice to have
• information about Cobalt Homes and QR codes. You can check out www.mycobalthomesagent.com

```html
<!DOCTYPE html>
<html lang="en">
<head>
<meta charset="utf-8">
<title>Cobalt Homes – Business Card</title>
<link rel="stylesheet" href="https://fonts.googleapis.com/css2?family=Cinzel:wght@700&family=Lora:wght@400;500&display=swap">
<style>
  :root {
    --backdrop: #e9e9ea;
    --card-dark: #1c1c1e;
    --card-light: #ffffff;
    --brand-blue: #2b84c4;
    --brand-ink: #222426;
    --logo-light: #cfe6f7;
    --text-light: #f2f2f2;
    --text-dark: #2a2a2a;
  }
  * { margin: 0; padding: 0; box-sizing: border-box; }
  html, body {
    width: 1200px; height: 715px; overflow: hidden;
    background: var(--backdrop);
    font-family: "Lora", serif;
  }
  .stage { position: relative; width: 1200px; height: 715px; }
  .card {
    position: absolute; width: 520px; height: 297px;
    border-radius: 4px; overflow: hidden;
    box-shadow: 0 8px 24px rgba(0,0,0,.18);
  }
  .brand { font-family: "Cinzel", serif; font-weight: 700; line-height: 1; }
  .brand-name { display: block; }
  .brand-sub { display: block; }

  /* Back side */
  .card-back { left: 50px; top: 130px; background: var(--card-dark); border-bottom: 5px solid var(--brand-blue); }
  .back-logo {
    position: absolute; left: 0; right: 0; top: 58px;
    text-align: center; color: var(--logo-light);
  }
  .back-logo .brand-name { font-size: 54px; letter-spacing: 2px; }
  .back-logo .brand-sub { font-size: 14px; letter-spacing: 16px; margin-top: 8px; padding-left: 16px; }
  .social-handle {
    position: absolute; left: 0; right: 0; top: 160px;
    text-align: center; color: var(--text-light); font-size: 12px; letter-spacing: 1px;
  }
  .office-list {
    position: absolute; left: 24px; right: 24px; bottom: 26px;
    display: flex; justify-content: space-between;
  }
  .office {
    color: var(--text-light); font-size: 12px; line-height: 1.5;
    padding: 0 14px; border-left: 1px solid var(--text-light);
  }
  .office:first-child { border-left: none; padding-left: 0; }

  /* Front side */
  .card-front { left: 630px; top: 270px; background: var(--card-light); }
  .front-wave { position: absolute; inset: 0; }
  .front-logo { position: absolute; left: 34px; top: 72px; color: var(--brand-ink); }
  .front-logo .brand-name { font-size: 40px; letter-spacing: 1px; }
  .front-logo .brand-sub { font-size: 11px; letter-spacing: 12px; margin-top: 6px; padding-left: 12px; }
  .logo-rule {
    position: absolute; left: 28px; top: 138px; width: 230px; height: 1px; background: var(--brand-blue);
  }
  .contact-list { position: absolute; left: 28px; top: 148px; list-style: none; }
  .contact-list li {
    display: flex; align-items: center; gap: 8px;
    font-size: 12px; color: var(--text-dark); line-height: 19px;
  }
  .contact-list svg { width: 10px; height: 10px; fill: var(--brand-blue); flex: none; }
  .agent {
    position: absolute; right: 26px; bottom: 16px; text-align: right;
    border-bottom: 1px solid var(--brand-blue); padding-bottom: 6px; width: 250px;
  }
  .agent-name { font-family: "Cinzel", serif; font-weight: 700; color: var(--brand-blue); font-size: 19px; letter-spacing: 1px; }
  .agent-title { color: var(--text-dark); font-size: 12px; }
</style>
</head>
<body>
<main class="stage">

  <section class="card card-back" aria-label="Business card back">
    <div class="brand back-logo">
      <span class="brand-name">COBALT</span>
      <span class="brand-sub">HOMES</span>
    </div>
    <p class="social-handle">Follow us @cobalthomes</p>
    <div class="office-list">
      <p class="office">410 Harbor Rd<br>Bayview, NY 10010</p>
      <p class="office">27 Elm Park Ave<br>Westfield, NY 10020</p>
      <p class="office">908 Maple St<br>Riverton, NY 10030</p>
    </div>
  </section>

  <section class="card card-front" aria-label="Business card front">
    <svg class="front-wave" viewBox="0 0 520 297" aria-hidden="true">
      <path d="M0 0 H520 V226 C440 218 385 193 345 138 C300 68 240 28 0 18 Z" fill="var(--brand-blue)"/>
      <path d="M0 18 C240 28 300 68 345 138 C385 193 440 218 520 226" fill="none" stroke="#ffffff" stroke-width="8"/>
      <path d="M0 25 C240 35 300 75 345 145 C385 200 440 225 520 233" fill="none" stroke="var(--brand-ink)" stroke-width="7"/>
    </svg>

    <div class="brand front-logo">
      <span class="brand-name">COBALT</span>
      <span class="brand-sub">HOMES</span>
    </div>
    <div class="logo-rule"></div>

    <ul class="contact-list">
      <li><svg viewBox="0 0 10 10"><path d="M2 0h2l1 3-1.5 1a6 6 0 0 0 2.5 2.5L7 5l3 1v2c0 1-1 2-2 2A8 8 0 0 1 0 2c0-1 1-2 2-2z"/></svg>555-310-4821</li>
      <li><svg viewBox="0 0 10 10"><path d="M2.5 0h5a1 1 0 0 1 1 1v8a1 1 0 0 1-1 1h-5a1 1 0 0 1-1-1V1a1 1 0 0 1 1-1zm0 1.5v6h5v-6z"/></svg>555-310-7364</li>
      <li><svg viewBox="0 0 10 10"><path d="M0 2h10v6H0zm1 1v.3l4 2.5 4-2.5V3z"/></svg>info@mycobalthomesagent.com</li>
      <li><svg viewBox="0 0 10 10"><circle cx="5" cy="5" r="5"/></svg>www.mycobalthomesagent.com</li>
    </ul>

    <div class="agent">
      <p class="agent-name">DANIEL RIVERA</p>
      <p class="agent-title">Associate Real Estate Broker</p>
    </div>
  </section>

</main>
</body>
</html>
```